Human Resources Flyer design

Create a 1 page flyer design for a staffing company that is looking to provide its services to clients. Images centered around people and businesses.
Target Market(s)
Large businesses
Industry/Entity Type
Staffing
Requirements
Must have
- Use color scheme that matches norvelhire.example.
Nice to have
- Flow chart like image for 3 areas mentioned.
- Images that convey professionalism and people connections

```html
<!DOCTYPE html>
<html lang="en">
<head>
<meta charset="utf-8">
<title>Norvel Hire – Services Flyer</title>
<link href="https://fonts.googleapis.com/css2?family=Arimo:ital,wght@0,400;0,700;1,700&family=PT+Sans:wght@400;700&display=swap" rel="stylesheet">
<style>
  :root {
    --backdrop: #7f7f7f;
    --paper: #ffffff;
    --brand-red: #bb2330;
    --ink-dark: #333333;
    --icon-ink: #2e2e2e;
    --text-light: #ffffff;
  }
  * { box-sizing: border-box; margin: 0; padding: 0; }
  html, body { width: 1200px; height: 1200px; overflow: hidden; background: var(--backdrop); }
  .flyer {
    position: absolute; left: 227px; top: 78px; width: 746px; height: 1046px;
    background: var(--paper); overflow: hidden;
    box-shadow: 0 2px 8px rgba(0,0,0,.35);
    font-family: "PT Sans", sans-serif;
  }
  .hero-photo {
    position: absolute; left: 0; top: 0; width: 746px; height: 426px;
    background: linear-gradient(160deg, #6d9fd6 0%, #a9c7e6 30%, #8c9299 55%, #4a5058 80%, #2d3a66 100%);
  }
  .brand-box {
    position: absolute; left: 455px; top: 13px; width: 291px; height: 98px;
    background: var(--paper); border-radius: 14px 0 0 14px;
    display: flex; align-items: center; justify-content: center; gap: 12px;
  }
  .brand-box .brand-dot { width: 22px; height: 22px; border-radius: 50%; background: var(--brand-red); }
  .brand-box .brand-name {
    font-family: "Arimo", sans-serif; font-weight: 700; font-size: 34px;
    color: var(--brand-red); letter-spacing: 1px;
  }
  .mission-quote {
    position: absolute; left: 37px; top: 440px; width: 690px;
    font-family: "Arimo", sans-serif; font-weight: 700; font-style: italic;
    font-size: 21.5px; line-height: 25.6px; color: var(--brand-red);
  }
  .mission-quote .mark { font-size: 40px; color: var(--ink-dark); line-height: 0; vertical-align: -6px; }
  .stage-flow {
    position: absolute; left: 0; top: 0; width: 188px; height: 1003px;
  }
  .stage-flow .flow-item { position: absolute; left: 0; width: 188px; text-align: center; }
  .stage-flow .flow-label {
    font-family: "Arimo", sans-serif; font-size: 16.5px; line-height: 20.5px; color: var(--brand-red);
  }
  .stage-flow svg { display: block; margin: 0 auto; }
  .services-panel {
    position: absolute; left: 191px; top: 581px; width: 555px; height: 422px;
    background: var(--brand-red); color: var(--text-light);
  }
  .panel-tab {
    position: absolute; left: 175px; top: 582px; width: 320px; height: 29px;
    background: var(--paper); border: 2px solid var(--brand-red); border-left-width: 3px;
    border-radius: 15px; padding-left: 24px;
    font-family: "Arimo", sans-serif; font-size: 16.5px; line-height: 25px; color: var(--brand-red);
  }
  .panel-intro { position: absolute; left: 198px; top: 618px; font-size: 11.5px; color: var(--text-light); }
  .stage { position: absolute; left: 175px; width: 560px; color: var(--text-light); }
  .stage-badge {
    position: absolute; left: 0; top: 0; width: 30px; height: 30px; border-radius: 50%;
    background: var(--ink-dark); border: 2px solid var(--paper);
    display: flex; align-items: center; justify-content: center;
  }
  .stage-title { position: absolute; left: 38px; top: 4px; font-family: "Arimo", sans-serif; font-weight: 700; font-size: 14.5px; }
  .stage-desc { position: absolute; left: 36px; width: 525px; font-size: 10.5px; line-height: 13px; }
  .stage-list { position: absolute; list-style: none; font-size: 10.5px; line-height: 16px; }
  .stage-list li { position: relative; padding-left: 11px; }
  .stage-list li::before { content: "➤"; position: absolute; left: 0; font-size: 7px; top: 0; }
  .site-band {
    position: absolute; left: 0; top: 1003px; width: 746px; height: 33px; background: var(--ink-dark);
    color: var(--text-light); text-align: center; font-size: 19px; line-height: 33px;
  }
  .base-strip { position: absolute; left: 191px; top: 1036px; width: 555px; height: 10px; background: var(--brand-red); }
</style>
</head>
<body>
<main class="flyer">
  <div class="hero-photo" role="img" aria-label="Photo of two engineers in hard hats and blue overalls reviewing plans beside industrial pipework under a blue sky"></div>
  <div class="brand-box">
    <span class="brand-dot"></span>
    <span class="brand-name">NORVEL HIRE</span>
  </div>

  <p class="mission-quote"><span class="mark">“</span> Our expertise in human resource management, risk mitigation and safety, payroll administration, workers’ compensation coverage and employee benefits allow our clients to focus on their core business <span class="mark">”</span></p>

  <div class="stage-flow">
    <div class="flow-item" style="top:590px">
      <svg width="44" height="44" viewBox="0 0 44 44" fill="none" stroke="#2e2e2e" stroke-width="2">
        <rect x="2" y="2" width="40" height="40"/><rect x="17" y="6" width="10" height="6" fill="#2e2e2e"/>
        <path d="M22 12v6M11 18h22M11 18v5M33 18v5"/><rect x="6" y="23" width="10" height="8"/><rect x="28" y="23" width="10" height="8"/>
        <path d="M6 37h32"/><circle cx="22" cy="37" r="2"/>
      </svg>
    </div>
    <div class="flow-item flow-label" style="top:658px">Tactical<br>Alignment</div>
    <div class="flow-item" style="top:702px">
      <svg width="24" height="30" viewBox="0 0 24 30" fill="none" stroke="#bb2330" stroke-width="2.5"><path d="M12 0v28M2 18l10 10 10-10"/></svg>
    </div>
    <div class="flow-item" style="top:750px">
      <svg width="42" height="42" viewBox="0 0 42 42">
        <circle cx="18" cy="18" r="13" fill="none" stroke="#2e2e2e" stroke-width="6" stroke-dasharray="5 3.2"/>
        <circle cx="18" cy="18" r="7" fill="none" stroke="#2e2e2e" stroke-width="3"/>
        <path d="M22 22l16 16" stroke="#2e2e2e" stroke-width="5" stroke-linecap="round"/>
      </svg>
    </div>
    <div class="flow-item flow-label" style="top:810px">Supervisor<br>Development</div>
    <div class="flow-item" style="top:850px">
      <svg width="24" height="30" viewBox="0 0 24 30" fill="none" stroke="#bb2330" stroke-width="2.5"><path d="M12 0v28M2 18l10 10 10-10"/></svg>
    </div>
    <div class="flow-item" style="top:898px">
      <svg width="44" height="46" viewBox="0 0 44 46" fill="#2e2e2e">
        <rect x="14" y="0" width="20" height="12" rx="2"/><circle cx="19" cy="6" r="1.5" fill="#fff"/><circle cx="24" cy="6" r="1.5" fill="#fff"/><circle cx="29" cy="6" r="1.5" fill="#fff"/>
        <circle cx="12" cy="19" r="5"/><circle cx="32" cy="19" r="5"/>
        <rect x="3" y="26" width="18" height="20" rx="4"/><rect x="23" y="26" width="18" height="20" rx="4"/>
      </svg>
    </div>
    <div class="flow-item flow-label" style="top:961px">Business-level<br>guidance</div>
  </div>

  <section class="services-panel"></section>
  <div class="panel-tab">What you can expect from Norvel</div>
  <p class="panel-intro">Business owners working with Norvel typically move through three stages.</p>

  <section class="stage" style="top:639px">
    <span class="stage-badge"><svg width="14" height="14" viewBox="0 0 14 14" fill="none" stroke="#fff" stroke-width="1.4"><rect x="1" y="1" width="12" height="12"/><path d="M7 3v3M4 6h6M4 6v3M10 6v3"/></svg></span>
    <h2 class="stage-title">Tactical Alignment</h2>
    <p class="stage-desc" style="top:29px;left:42px">The first stage addresses the administrative and tactical components of managing your employees.</p>
    <ul class="stage-list" style="top:51px;left:42px">
      <li>Analysis of safety programs and HR practices</li>
      <li>Establish payroll submission and administration protocol</li>
      <li>Hiring, selection and new hire onboarding best practices</li>
    </ul>
    <ul class="stage-list" style="top:51px;left:332px">
      <li>Injury reporting protocol</li>
      <li>Establishing goals and creation of action plan</li>
      <li>Identification of metrics to track effectiveness</li>
    </ul>
  </section>

  <section class="stage" style="top:738px">
    <span class="stage-badge"><svg width="14" height="14" viewBox="0 0 14 14" fill="none" stroke="#fff" stroke-width="1.6"><circle cx="6" cy="6" r="4"/><path d="M9 9l4 4"/></svg></span>
    <h2 class="stage-title">Supervisor Development</h2>
    <p class="stage-desc" style="top:30px">The second stage of the relationship focuses on continuing process improvement, further development of HR, risk and payroll best practices, as well as supervisor development.&nbsp; Examples include:</p>
    <ul class="stage-list" style="top:65px;left:36px;width:270px">
      <li>Ongoing development and refinement of action plans</li>
      <li>Supervisory skill development and training (workplace</li>
      <li style="line-height:13px;margin-top:2px">safety, effective human capital management, and overall risk mitigation)</li>
    </ul>
    <ul class="stage-list" style="top:65px;left:325px">
      <li>Platform of performance management and</li>
      <li>performance improvement</li>
      <li>Evaluation of employee benefits options</li>
    </ul>
  </section>

  <section class="stage" style="top:868px">
    <span class="stage-badge"><svg width="14" height="14" viewBox="0 0 14 14" fill="#fff"><circle cx="4" cy="6" r="2"/><circle cx="10" cy="6" r="2"/><rect x="1" y="9" width="6" height="5" rx="1"/><rect x="7" y="9" width="6" height="5" rx="1"/><rect x="5" y="0" width="6" height="3"/></svg></span>
    <h2 class="stage-title" style="left:34px">Business-level guidance</h2>
    <p class="stage-desc" style="top:21px;left:34px">Activities involved in the third stage of the relationship are more strategic and forward-looking with a goal of cultivating an environment in your organization in which employees and supervisors drive the success of the organization instead of you, the business owner. Areas of focus may include:</p>
    <ul class="stage-list" style="top:73px;left:34px">
      <li>Strategic planning</li>
      <li>Proactive mitigation of business risks</li>
      <li>Holistic view of where your business is going</li>
    </ul>
    <ul class="stage-list" style="top:76px;left:325px;width:215px">
      <li style="line-height:13px;margin-bottom:3px">Leadership development and succession planning</li>
      <li>Organizational development and design</li>
    </ul>
  </section>

  <footer class="site-band">www.norvelhire.example</footer>
  <div class="base-strip"></div>
</main>
</body>
</html>
```